Stationery Design Project

Brisk-Span Consultants is interim management company. We are specialized in finding the best Finance and IT consultants for our clients when they require additional resources on an interim basis for projects or special situations. We are flexible in our approach and we always seek to maximize the benefits for our clients as well as our consultants.

We are looking for a design of our letterhead, general stationery and business cards using the company name. The design will also be found on our coming web pages.
Updates

Please also create a logo for Brisk-Span Consultants which expresses that we want to match the best finance and IT people to our customers projects

Target Market(s)

Larger and mid sized companies (all sectors), as well as highly skilled Finance & IT professionals/consultants

Industry/Entity Type

Business

Requirements
Must have
• Brisk-Span Consultants
We are expecting that 'Brisk-Span' will be on the first line and 'Consultants' on a second line.
Please also indicate style of the letters for our address/phone and mail details. Our current address is:
Tornagervej 14,
2915 Skovlunde
Danmark
Mobile: +45 XX XX XX XX Mail: xx@brisk-span.dk

```html
<!DOCTYPE html>
<html lang="en">
<head>
<meta charset="utf-8">
<title>Brisk-Span Consultants – Business Card</title>
<link rel="stylesheet" href="https://fonts.googleapis.com/css2?family=Arimo:wght@700&display=swap">
<style>
  :root {
    --stage: #000000;
    --card-light: #3d69c0;
    --card-mid: #2d54a8;
    --card-dark: #1d3a87;
    --ink: #ffffff;
    --rule: #1b2a55;
  }
  * { margin: 0; padding: 0; box-sizing: border-box; }
  html, body {
    width: 1200px;
    height: 900px;
    overflow: hidden;
    background: var(--stage);
  }
  body {
    position: relative;
    font-family: "Arimo", Arial, sans-serif;
    font-weight: 700;
    color: var(--ink);
  }
  .card {
    position: absolute;
    top: 200px;
    width: 576px;
    height: 371px;
    overflow: hidden;
  }
  .card--front { left: 13px; }
  .card--back { left: 606px; }
  .card__surface {
    position: absolute;
    inset: 0;
    background: radial-gradient(ellipse at 50% 45%, var(--card-light) 0%, var(--card-mid) 50%, var(--card-dark) 100%);
  }
  .wordmark {
    position: absolute;
    text-align: center;
    line-height: 1;
  }
  .wordmark__name { display: block; }
  .wordmark__tag {
    display: block;
    letter-spacing: 0.36em;
    margin-right: -0.36em;
  }
  .card--front .wordmark { left: 0; right: 0; top: 143px; }
  .card--front .wordmark__name { font-size: 52px; }
  .card--front .wordmark__tag { font-size: 15px; margin-top: 12px; }
  .card--back .wordmark { left: 40px; width: 220px; top: 158px; }
  .card--back .wordmark__name { font-size: 33px; }
  .card--back .wordmark__tag { font-size: 14px; margin-top: 8px; }
  .card__divider {
    position: absolute;
    left: 289px;
    top: 92px;
    width: 3px;
    height: 185px;
    background: var(--rule);
  }
  .contact {
    position: absolute;
    left: 337px;
    top: 142px;
    font-size: 16px;
    line-height: 18.5px;
    font-style: normal;
  }
</style>
</head>
<body>
  <section class="card card--front">
    <div class="card__surface" role="img" aria-label="Blue background with a fine dot grid pattern"></div>
    <h1 class="wordmark">
      <span class="wordmark__name">BRISK-SPAN</span>
      <span class="wordmark__tag">CONSULTANTS</span>
    </h1>
  </section>

  <section class="card card--back">
    <div class="card__surface" role="img" aria-label="Blue background with a fine dot grid pattern"></div>
    <div class="wordmark">
      <span class="wordmark__name">BRISK-SPAN</span>
      <span class="wordmark__tag">CONSULTANTS</span>
    </div>
    <div class="card__divider"></div>
    <address class="contact">
      Tornagervej 14<br>
      2915 Skovlunde<br>
      Danmark<br>
      Mobile: +45 XX XX XX XX<br>
      Mail: xx@brisk-span.dk
    </address>
  </section>
</body>
</html>
```